Menu Design Project for an Italian cafe

Casual Italian style cafe situated in Chinatown in Sydney Australia . Value for money food, good coffee and good location are the cafes strengths. Catering to bushiness crowd in the morning/lunch, tourist crowd for brunch and Asian customers for late afternoon coffee.
Design concept is understated, casual European chic. Should communicate a casual escape to have a good meet up with friends to escape the hustle and bustle of the city crowd.
Would like to move away from current colors of dark brown, creme, black and orange. Would like a more enticing vibrant and brighter colour scheme.
Industry/Entity Type
Cafe
Look and feel
Each slider illustrates characteristics of the customer's brand and the style your logo design should communicate.

```html
<!DOCTYPE html>
<html lang="en">
<head>
<meta charset="utf-8">
<title>Basilico Cafe Restaurant – Menu</title>
<link rel="stylesheet" href="https://fonts.googleapis.com/css2?family=Kaushan+Script&family=Tinos:wght@400&display=swap">
<style>
  :root {
    --teal: #0e9d97;
    --white: #ffffff;
    --produce-light: #c9a59a;
    --produce-dark: #9a5a55;
    --cup-light: #b9a284;
    --cup-dark: #7a5a44;
  }
  html, body {
    margin: 0;
    padding: 0;
    overflow: hidden;
    background: var(--teal);
  }
  .menu {
    position: relative;
    width: 939px;
    height: 1200px;
    overflow: hidden;
    background: var(--teal);
    color: var(--white);
    font-family: "Tinos", "Times New Roman", serif;
  }
  .brand {
    position: absolute;
    left: 257px;
    top: 28px;
    display: flex;
    align-items: center;
    gap: 22px;
  }
  .brand-dot {
    width: 134px;
    height: 134px;
    border: 4px solid var(--white);
    border-radius: 50%;
    box-sizing: border-box;
  }
  .brand-text {
    display: flex;
    flex-direction: column;
    align-items: flex-end;
  }
  .brand-name {
    font-size: 70px;
    line-height: 1;
    color: var(--white);
  }
  .brand-tag {
    margin-top: 8px;
    font-size: 19px;
    letter-spacing: 2px;
  }
  .section-title {
    position: absolute;
    margin: 0;
    font-family: "Kaushan Script", "Brush Script MT", cursive;
    font-weight: 400;
    line-height: 60px;
    text-align: center;
    white-space: nowrap;
  }
  .title-pasta { left: 70px; top: 232px; width: 500px; font-size: 56px; }
  .title-drinks { left: 420px; top: 738px; width: 440px; font-size: 55px; }
  .photo {
    position: absolute;
    border-radius: 50%;
  }
  .photo-produce {
    left: 543px; top: 297px; width: 392px; height: 392px;
    background: linear-gradient(180deg, var(--produce-light) 0%, var(--produce-dark) 100%);
  }
  .photo-cup {
    left: -29px; top: 732px; width: 464px; height: 464px;
    background: linear-gradient(180deg, var(--cup-light) 0%, var(--cup-dark) 100%);
  }
  .price-list {
    position: absolute;
    left: 0; top: 0;
    margin: 0; padding: 0;
    list-style: none;
    font-size: 15px;
  }
  .price-list li {
    position: absolute;
    left: var(--x);
    top: var(--y);
    width: var(--w);
    display: flex;
    align-items: baseline;
    line-height: 20px;
  }
  .leader {
    flex: 1;
    border-bottom: 2px dotted var(--white);
    margin: 0 1px;
    transform: translateY(-3px);
  }
</style>
</head>
<body>
<main class="menu">
  <header class="brand">
    <div class="brand-dot"></div>
    <div class="brand-text">
      <span class="brand-name">Basilico</span>
      <span class="brand-tag">CAFE RESTAURANT</span>
    </div>
  </header>

  <h2 class="section-title title-pasta">Pasta, Soup,<br>Salad, and More!</h2>
  <div class="photo photo-produce" role="img" aria-label="Photo of fresh tomato, red onion, garlic and dry pasta"></div>

  <ul class="price-list pasta-list">
    <li style="--x:101px;--y:384px;--w:460px"><span>Pasta</span><span class="leader"></span><span>1.75</span></li>
    <li style="--x:90px;--y:405px;--w:458px"><span>Pasta</span><span class="leader"></span><span>1.75</span></li>
    <li style="--x:83px;--y:426px;--w:460px"><span>Pasta</span><span class="leader"></span><span>1.75</span></li>
    <li style="--x:78px;--y:447px;--w:461px"><span>Pasta</span><span class="leader"></span><span>1.75</span></li>
    <li style="--x:78px;--y:468px;--w:461px"><span>Pasta</span><span class="leader"></span><span>1.75</span></li>
    <li style="--x:78px;--y:489px;--w:461px"><span>Pasta</span><span class="leader"></span><span>1.75</span></li>
    <li style="--x:78px;--y:510px;--w:461px"><span>Pasta</span><span class="leader"></span><span>1.75</span></li>
    <li style="--x:78px;--y:531px;--w:461px"><span>Pasta</span><span class="leader"></span><span>1.75</span></li>
    <li style="--x:83px;--y:552px;--w:460px"><span>Pasta</span><span class="leader"></span><span>1.75</span></li>
    <li style="--x:90px;--y:573px;--w:461px"><span>Pasta</span><span class="leader"></span><span>1.75</span></li>
    <li style="--x:99px;--y:594px;--w:462px"><span>Pasta</span><span class="leader"></span><span>1.75</span></li>
    <li style="--x:110px;--y:615px;--w:462px"><span>Pasta</span><span class="leader"></span><span>1.75</span></li>
  </ul>

  <h2 class="section-title title-drinks">Coffee and Drinks!</h2>
  <div class="photo photo-cup" role="img" aria-label="Photo of a ceramic coffee cup"></div>

  <ul class="price-list coffee-list">
    <li style="--x:406px;--y:842px;--w:400px"><span>Coffee</span><span class="leader"></span><span>1.90</span></li>
    <li style="--x:414px;--y:863px;--w:402px"><span>Coffee</span><span class="leader"></span><span>1.90</span></li>
    <li style="--x:420px;--y:884px;--w:402px"><span>Coffee</span><span class="leader"></span><span>1.90</span></li>
    <li style="--x:425px;--y:905px;--w:401px"><span>Coffee</span><span class="leader"></span><span>1.90</span></li>
    <li style="--x:427px;--y:926px;--w:402px"><span>Coffee</span><span class="leader"></span><span>1.90</span></li>
    <li style="--x:429px;--y:947px;--w:400px"><span>Coffee</span><span class="leader"></span><span>1.90</span></li>
    <li style="--x:429px;--y:968px;--w:400px"><span>Coffee</span><span class="leader"></span><span>1.90</span></li>
    <li style="--x:429px;--y:989px;--w:400px"><span>Coffee</span><span class="leader"></span><span>1.90</span></li>
    <li style="--x:426px;--y:1010px;--w:400px"><span>Coffee</span><span class="leader"></span><span>1.90</span></li>
    <li style="--x:420px;--y:1031px;--w:402px"><span>Coffee</span><span class="leader"></span><span>1.90</span></li>
    <li style="--x:413px;--y:1052px;--w:401px"><span>Coffee</span><span class="leader"></span><span>1.90</span></li>
    <li style="--x:403px;--y:1073px;--w:401px"><span>Coffee</span><span class="leader"></span><span>1.90</span></li>
  </ul>
</main>
</body>
</html>
```